Moving Company Needs Business Card Design

We need a business cars for moving company based in San Diego. We are called Harborline Relocation Group. We move locally and long distance. 1st side: Logo, website: www.HarborlineRelo.com, Telephone number: 1-855-314-7068.
2nd side: Licensed and Insured,
We move homes and businesses
Services: Local Moving, Long Distance Moving, Loading / Unloading your truck / container, On-site Moving, Packing Service
telephone number 1-855-314-7068, email: info@harborlinerelo.com

```html
<!DOCTYPE html>
<html lang="en">
<head>
<meta charset="utf-8">
<title>Harborline Relocation Group – Business Card</title>
<link href="https://fonts.googleapis.com/css2?family=Montserrat:wght@600;700;800&family=Open+Sans:wght@400;600&display=swap" rel="stylesheet">
<style>
  :root {
    --navy: #1b3a78;
    --red: #d81e27;
    --white: #ffffff;
    --stage: #2a2828;
    --ink-light: #dfe6f3;
  }
  html, body {
    margin: 0;
    width: 1200px;
    height: 901px;
    overflow: hidden;
    background: var(--stage);
  }
  .card {
    position: absolute;
    left: 250px;
    width: 700px;
    height: 400px;
    background: var(--white);
    overflow: hidden;
    box-shadow: 0 6px 18px rgba(0,0,0,.45);
  }
  .card--front { top: 30px; }
  .card--back { top: 471px; }
  .card__shapes { position: absolute; inset: 0; }
  .brand-name {
    position: absolute;
    font-family: "Montserrat", sans-serif;
    font-weight: 800;
    color: var(--red);
    text-transform: uppercase;
    letter-spacing: .5px;
    line-height: 1.05;
    margin: 0;
  }
  .card--front .brand-name {
    left: 60px;
    top: 58px;
    font-size: 40px;
  }
  .card--back .brand-name {
    right: 34px;
    top: 26px;
    font-size: 19px;
    text-align: right;
  }
  .contact {
    position: absolute;
    display: flex;
    align-items: center;
    gap: 10px;
    font-family: "Montserrat", sans-serif;
    font-weight: 700;
    color: var(--white);
    margin: 0;
  }
  .contact svg { flex: none; fill: var(--white); }
  .card--front .contact--phone { right: 34px; top: 262px; font-size: 24px; }
  .card--front .contact--web { left: 50px; top: 338px; font-size: 23px; }
  .tagline {
    position: absolute;
    left: 34px;
    top: 34px;
    margin: 0;
    font-family: "Montserrat", sans-serif;
    font-weight: 800;
    font-size: 16px;
    line-height: 1.3;
    color: var(--navy);
    text-transform: uppercase;
  }
  .services {
    position: absolute;
    left: 48px;
    top: 170px;
    width: 560px;
    color: var(--white);
  }
  .services__title {
    margin: 0 0 4px;
    font-family: "Montserrat", sans-serif;
    font-weight: 700;
    font-size: 26px;
  }
  .services__list {
    margin: 0;
    font-family: "Open Sans", sans-serif;
    font-size: 17px;
    line-height: 1.35;
    color: var(--ink-light);
  }
  .card--back .contact { position: static; font-size: 20px; margin-top: 8px; }
  .services__contacts { margin-top: 12px; }
</style>
</head>
<body>

<section class="card card--front" aria-label="Card front">
  <svg class="card__shapes" width="700" height="400" viewBox="0 0 700 400" aria-hidden="true">
    <path d="M0 300 Q350 250 700 170 L700 182 Q350 262 0 312 Z" fill="var(--red)"/>
    <path d="M0 320 Q350 270 700 190 L700 400 L0 400 Z" fill="var(--navy)"/>
  </svg>
  <h1 class="brand-name">Harborline<br>Relocation Group</h1>
  <p class="contact contact--phone">
    <svg width="20" height="20" viewBox="0 0 24 24" aria-hidden="true"><path d="M6.6 10.8a15.1 15.1 0 0 0 6.6 6.6l2.2-2.2c.3-.3.7-.4 1-.2 1.1.4 2.3.6 3.6.6.6 0 1 .4 1 1V20c0 .6-.4 1-1 1A17 17 0 0 1 3 4c0-.6.4-1 1-1h3.5c.6 0 1 .4 1 1 0 1.3.2 2.5.6 3.6.1.3 0 .7-.2 1z"/></svg>
    1-855-314-7068
  </p>
  <p class="contact contact--web">
    <svg width="20" height="20" viewBox="0 0 24 24" aria-hidden="true"><path d="M12 2a10 10 0 1 0 0 20 10 10 0 0 0 0-20zm6.9 6h-2.9a15.7 15.7 0 0 0-1.4-3.6A8 8 0 0 1 18.9 8zM12 4c.8 1.2 1.5 2.5 1.9 4h-3.8c.4-1.5 1.1-2.8 1.900-4zM4.3 14a8 8 0 0 1 0-4h3.4a16.5 16.5 0 0 0 0 4zm.8 2h2.9c.3 1.3.8 2.5 1.4 3.6A8 8 0 0 1 5.1 16zM8 8H5.1a8 8 0 0 1 4.3-3.6C8.8 5.5 8.3 6.7 8 8zm4 12c-.8-1.2-1.5-2.5-1.9-4h3.8c-.4 1.5-1.1 2.8-1.9 4zm2.3-6H9.7a14.7 14.7 0 0 1 0-4h4.6a14.7 14.7 0 0 1 0 4zm.3 5.6c.6-1.1 1.1-2.3 1.4-3.6h2.9a8 8 0 0 1-4.3 3.6zm1.7-5.6a16.5 16.5 0 0 0 0-4h3.4a8 8 0 0 1 0 4z"/></svg>
    www.HarborlineRelo.com
  </p>
</section>

<section class="card card--back" aria-label="Card back">
  <svg class="card__shapes" width="700" height="400" viewBox="0 0 700 400" aria-hidden="true">
    <path d="M0 128 Q350 120 700 58 L700 70 Q350 132 0 140 Z" fill="var(--red)"/>
    <path d="M0 148 Q350 140 700 78 L700 400 L0 400 Z" fill="var(--navy)"/>
  </svg>
  <p class="tagline">Licensed and insured,<br>we move homes and businesses</p>
  <p class="brand-name">Harborline<br>Relocation Group</p>
  <div class="services">
    <h2 class="services__title">Services:</h2>
    <p class="services__list">Local Moving, Long Distance Moving,<br>Loading / Unloading your truck / container,<br>On-site Moving, Packing Service</p>
    <div class="services__contacts">
      <p class="contact">
        <svg width="18" height="18" viewBox="0 0 24 24" aria-hidden="true"><path d="M6.6 10.8a15.1 15.1 0 0 0 6.6 6.6l2.2-2.2c.3-.3.7-.4 1-.2 1.1.4 2.3.6 3.6.6.6 0 1 .4 1 1V20c0 .6-.4 1-1 1A17 17 0 0 1 3 4c0-.6.4-1 1-1h3.5c.6 0 1 .4 1 1 0 1.3.2 2.5.6 3.6.1.3 0 .7-.2 1z"/></svg>
        1-855-314-7068
      </p>
      <p class="contact">
        <svg width="18" height="18" viewBox="0 0 24 24" aria-hidden="true"><path d="M2 5h20v14H2zm2 2v.5l8 5 8-5V7zm0 2.8V17h16V9.8l-8 5z"/></svg>
        info@harborlinerelo.com
      </p>
    </div>
  </div>
</section>

</body>
</html>
```